Non-profit organization requires InDesign based template for a educational booklet

***Overview***
Our business "The Southern Meridian Collective for Skills and Growth" is a not for profit organisation working in vocational education both in the Australian and international markets. While we work within many professional contexts, we also work with projects in developing countries assisting to build institutional capacity in the education industry, upskilling in disadvantaged communities to ultimately facilitate positive development outcomes.

Our project is looking to deliver agricultural-based education units that will be delivered in booklet form. Vocational students will use these unit booklets for self-paced or classroom group study. The front of each unit will have a nice graphical cover page, contents and details about learning in the unit. This will be followed by about 15 pages of educational content with plenty of pictures and other material such as tables and graphs to illustrate learning points. This will then be followed by a short question sheet with space for students to write answers, followed by Activity sheets where students put into practice skills from the unit.

***The designed template should have***
* Cover page;
* Content page;
* Two (2) different introduction pages (two for variation);
* Three (3) different pages for lesson text – these pages will be the main study pages for the students, 3 for variation;
* Activity page - like an activity worksheet;
* Question page - page with questions or reflections that the students need to answer - a space under each question for students to write;

***Design preferences***

*Font – an inDesign default font please like Calibri – text built on a base Normal font 11pt, then headings H1, H2 etc... from that basis e.g. 24pt for H1 etc... the size up to the designer.

Happy to see creativity of graphic artists with the above themes.

Target Market(s)

In the requested project, I require an Adobe InDesign template (file in .indd) to be designed that will have particular characteristics suited to students who are:

* Age 15-17;
* Have the educational equivalent to Australian and US education standard of Yr 8;
* Attending vocational school - vocational schools are between secondary high school and University and are usually used to produce graduates within the skill trade area;
* Agricultural theme in the template;
* Sustainability theme (agricultural sustainability) as well;

Students are from very poor rural farming families in growing rice, coconut, rambutan, mangoes, cocoa, palm oil... - very SE Asian agricultural landscape.

Students are used to black and white government textbooks which are very dry, largely dull in design and colour – we do not want this!

Industry/Entity Type

Agriculture

Font styles to use
Sans Serif

Colors

Designer to choose colors to be used in the design.

Requirements
Must have
• * Final file must be in an editable Adobe Indesign file (.indd), with editable layers;
• * SE Asian agricultural theme in the template;
• * design must not look like dull and boring textbooks or corporate training booklets; * design should be vibrant and interesting but also not distracting from the lesson (i.e. it is not too garish);
• * suitable colours (it will be printed full colour) easy on the eye for students of the age group - colours related to agriculture;
• *Modern look and feel;
Should not have
• * design must not look like dull and boring textbooks or corporate training booklets;

```html
<!DOCTYPE html>
<html lang="en">
<head>
<meta charset="utf-8">
<title>Agricultural Unit Booklet Template</title>
<link rel="stylesheet" href="https://fonts.googleapis.com/css2?family=Carlito:wght@400;700&display=swap">
<style>
  :root {
    --backdrop-top: #a9c46e;
    --backdrop-bottom: #cfe0a0;
    --cream: #f5f2e0;
    --paper: #ffffff;
    --green-dark: #2f7a2c;
    --green-title: #2b6e2a;
    --green: #5fae2e;
    --lime: #a8d13a;
    --lime-light: #c9e26a;
    --orange: #ee7a1f;
    --brand-blue: #2a84c2;
    --ink: #3a3a3a;
    --muted: #6a6a6a;
    --rule: #9a9a9a;
  }
  * { box-sizing: border-box; margin: 0; padding: 0; }
  html, body { width: 1200px; height: 2486px; overflow: hidden; }
  body {
    position: relative;
    font-family: "Carlito", "Calibri", sans-serif;
    color: var(--ink);
    background: linear-gradient(180deg, var(--backdrop-top), var(--backdrop-bottom));
  }
  .gradient-defs { position: absolute; width: 0; height: 0; }

  .spread {
    position: absolute;
    left: 100px;
    width: 1000px;
    height: 707px;
    display: flex;
    box-shadow: 0 18px 40px rgba(40, 60, 10, 0.28);
  }
  .spread--covers { top: 90px; }
  .spread--contents { top: 889px; }
  .spread--intro { top: 1688px; }

  .page {
    position: relative;
    width: 500px;
    height: 707px;
    overflow: hidden;
    background: var(--cream);
  }
  .page--blank { background: var(--paper); }
  .page--left::after, .page--right::after {
    content: "";
    position: absolute; top: 0; bottom: 0; width: 26px;
    pointer-events: none;
  }
  .page--left::after { right: 0; background: linear-gradient(90deg, transparent, rgba(0,0,0,0.07)); }
  .page--right::after { left: 0; background: linear-gradient(90deg, rgba(0,0,0,0.07), transparent); }

  /* Footer wave */
  .footer-wave {
    position: absolute; left: 0; bottom: 0;
    width: 500px; height: 150px;
  }

  /* Brand lockup */
  .brand { position: absolute; display: flex; align-items: center; gap: 8px; z-index: 2; }
  .brand-dot {
    width: 16px; height: 16px; border-radius: 50%;
    background: var(--lime); flex: none;
  }
  .brand-name {
    font-weight: 700; font-size: 13px; line-height: 1.1;
    color: var(--brand-blue);
  }
  .brand--light .brand-dot { background: #ffffff; }
  .brand--light .brand-name { color: #ffffff; font-size: 11px; }

  /* Back cover */
  .back-brand { left: 70px; top: 100px; }
  .back-brand .brand-name { font-size: 16px; }
  .back-brand .brand-dot { width: 22px; height: 22px; }
  .back-contact {
    position: absolute; left: 70px; top: 170px;
    font-size: 11px; line-height: 1.5; color: var(--muted);
  }
  .back-contact strong { color: var(--ink); }
  .map-area {
    position: absolute; left: 0; top: 240px; width: 500px; height: 420px;
    background: linear-gradient(160deg, #e6ecd9 0%, #d8e6cc 40%, #e9e6dc 70%, #cfe2c2 100%);
  }
  .map-pin {
    position: absolute; left: 218px; top: 372px;
    width: 22px; height: 30px;
  }

  /* Front cover */
  .front-cover { background: linear-gradient(180deg, #e3ede4 0%, #cfe1d6 35%, #b9d2c1 55%); }
  .front-brand { left: 50%; top: 60px; transform: translateX(-50%); }
  .cover-title {
    position: absolute; left: 0; right: 0; top: 150px;
    text-align: center;
    font-size: 40px; font-weight: 700; letter-spacing: 0.5px;
    color: var(--green-title);
  }
  .cover-ribbon {
    position: absolute; left: 50%; top: 200px; transform: translateX(-50%);
    padding: 6px 34px;
    background: var(--orange); color: #ffffff;
    font-size: 15px; font-weight: 700; letter-spacing: 1px;
    clip-path: polygon(0 0, 100% 0, 94% 50%, 100% 100%, 0 100%, 6% 50%);
  }
  .cover-photo {
    position: absolute; left: 0; top: 300px; width: 500px; height: 407px;
    background: linear-gradient(175deg, #bcd4a8 0%, #9dc24a 30%, #7fae2a 55%, #5c8a22 80%, #3f6b1c 100%);
  }

  /* Contents page */
  .page-title {
    position: absolute; left: 0; right: 0; top: 48px;
    text-align: center;
    font-size: 24px; font-weight: 700; color: var(--green-title);
  }
  .toc {
    position: absolute; left: 70px; right: 60px; top: 120px;
    list-style: none; font-size: 13px;
  }
  .toc-item { display: flex; align-items: baseline; height: 26px; }
  .toc-leader { flex: 1; border-bottom: 1.5px dotted var(--rule); margin: 0 4px; transform: translateY(-3px); }
  .crop-circle { position: absolute; border-radius: 50%; }
  .crop-circle--rambutan { left: 18px; top: 300px; width: 180px; height: 180px;
    background: radial-gradient(circle at 40% 40%, #d8344a, #a31a2c 60%, #5e1a1a); }
  .crop-circle--rice { left: 258px; top: 270px; width: 150px; height: 150px;
    background: radial-gradient(circle at 45% 40%, #f2ead4, #dccfa8 70%, #c6b78c); }
  .crop-circle--cocoa { left: 245px; top: 412px; width: 185px; height: 185px;
    background: radial-gradient(circle at 45% 40%, #b86a48, #8a4a30 60%, #5c2e1e); }
  .crop-circle--mango { left: 165px; top: 480px; width: 90px; height: 90px;
    background: radial-gradient(circle at 45% 40%, #f3d48a, #d8a44a 60%, #6a8a3a); }
  .accent-dot { position: absolute; left: -20px; top: 500px; width: 70px; height: 70px;
    border-radius: 50%; background: var(--lime); }
  .contents-brand { right: 30px; bottom: 20px; }

  /* Intro pages */
  .body-text {
    position: absolute;
    font-size: 9.5px; line-height: 1.42; color: var(--ink);
    text-align: justify; text-indent: 3em;
  }
  .intro-lead { left: 50px; right: 50px; top: 100px; }
  .terrace-photo {
    position: absolute; left: 50px; top: 205px; width: 165px; height: 300px;
    background: linear-gradient(180deg, #dfe6d8 0%, #b7cf9a 30%, #7ea84a 60%, #5b8b2c 100%);
  }
  .intro-column { left: 230px; right: 50px; top: 205px; }
  .intro-left-brand { left: 40px; bottom: 22px; }

  .profile {
    position: absolute; left: 40px; right: 50px;
    display: flex; gap: 14px;
  }
  .profile:nth-of-type(1) { top: 100px; }
  .profile:nth-of-type(2) { top: 184px; }
  .profile:nth-of-type(3) { top: 268px; }
  .portrait {
    flex: none; width: 68px; height: 72px;
    border: 2px solid #ffffff; outline: 1px solid #c9c9c9;
    background: linear-gradient(180deg, #f4f4f4 0%, #d9d9d9 60%, #4a4a4a 100%);
  }
  .profile-body { flex: 1; padding-top: 2px; }
  .profile-name { font-size: 10.5px; margin-bottom: 8px; color: var(--ink); }
  .profile-name strong { color: var(--orange); font-weight: 700; }
  .profile-text { font-size: 9.5px; line-height: 1.42; text-align: justify; text-indent: 3em; }
  .intro-closing { left: 50px; right: 50px; top: 360px; }
  .intro-closing p + p { margin-top: 6px; }
  .intro-right-brand { right: 30px; bottom: 22px; }
</style>
</head>
<body>

<svg class="gradient-defs" aria-hidden="true">
  <defs>
    <linearGradient id="wave-fill" x1="0" y1="0" x2="1" y2="1">
      <stop offset="0" stop-color="#b6d940"/>
      <stop offset="1" stop-color="#7fbf2e"/>
    </linearGradient>
  </defs>
</svg>

<!-- Covers -->
<section class="spread spread--covers">
  <article class="page page--left back-cover">
    <div class="brand back-brand">
      <span class="brand-dot"></span>
      <span class="brand-name">The Southern Meridian Collective<br>for Skills and Growth</span>
    </div>
    <p class="back-contact">
      Level 4, 28 Harbour Lane, Brookvale, NSW 2100<br>
      <strong>+61 (2) 9555 0148 &nbsp;|&nbsp; www.southernmeridian.edu.au</strong>
    </p>
    <div class="map-area" role="img" aria-label="Street map showing the office location"></div>
    <svg class="map-pin" viewBox="0 0 22 30" aria-hidden="true">
      <path d="M11 0C5 0 0 5 0 11c0 8 11 19 11 19s11-11 11-19C22 5 17 0 11 0z" fill="#d6322f"/>
      <circle cx="11" cy="11" r="4" fill="#ffffff"/>
    </svg>
    <svg class="footer-wave" viewBox="0 0 500 150" preserveAspectRatio="none" aria-hidden="true">
      <path d="M0 40 C120 110 330 120 500 20 L500 150 L0 150 Z" fill="var(--green-dark)"/>
      <path d="M0 52 C120 120 330 130 500 32 L500 150 L0 150 Z" fill="url(#wave-fill)"/>
    </svg>
  </article>

  <article class="page page--right front-cover">
    <div class="brand front-brand">
      <span class="brand-dot"></span>
      <span class="brand-name">The Southern Meridian Collective<br>for Skills and Growth</span>
    </div>
    <h1 class="cover-title">HEAD LINE TITLE</h1>
    <div class="cover-ribbon">CAPTION SUB TITLE</div>
    <div class="cover-photo" role="img" aria-label="Photograph of green rice terraces with a small farm hut"></div>
  </article>
</section>

<!-- Contents -->
<section class="spread spread--contents">
  <article class="page page--left page--blank"></article>

  <article class="page page--right contents-page">
    <h2 class="page-title">Content</h2>
    <ol class="toc">
      <li class="toc-item"><span>Introduction</span><span class="toc-leader"></span><span>1</span></li>
      <li class="toc-item"><span>Lesson 1</span><span class="toc-leader"></span><span>3</span></li>
      <li class="toc-item"><span>Lesson 2</span><span class="toc-leader"></span><span>4</span></li>
      <li class="toc-item"><span>Lesson 3</span><span class="toc-leader"></span><span>5</span></li>
      <li class="toc-item"><span>Activity</span><span class="toc-leader"></span><span>6</span></li>
      <li class="toc-item"><span>Question</span><span class="toc-leader"></span><span>7</span></li>
    </ol>
    <div class="crop-circle crop-circle--rambutan" role="img" aria-label="Photograph of fresh rambutan fruit"></div>
    <div class="crop-circle crop-circle--rice" role="img" aria-label="Photograph of raw rice grains"></div>
    <div class="crop-circle crop-circle--cocoa" role="img" aria-label="Photograph of dried cocoa beans"></div>
    <div class="crop-circle crop-circle--mango" role="img" aria-label="Photograph of small yellow mangoes"></div>
    <svg class="footer-wave" viewBox="0 0 500 150" preserveAspectRatio="none" aria-hidden="true">
      <path d="M0 40 C150 120 350 100 500 20 L500 150 L0 150 Z" fill="var(--green-dark)"/>
      <path d="M0 52 C150 132 350 112 500 32 L500 150 L0 150 Z" fill="url(#wave-fill)"/>
    </svg>
    <div class="accent-dot"></div>
    <div class="brand brand--light contents-brand">
      <span class="brand-dot"></span>
      <span class="brand-name">The Southern Meridian Collective<br>for Skills and Growth</span>
    </div>
  </article>
</section>

<!-- Introduction -->
<section class="spread spread--intro">
  <article class="page page--left intro-page">
    <h2 class="page-title">Introduction</h2>
    <p class="body-text intro-lead">Farming families across the region grow rice, coconut, cocoa and fruit on small plots of land. This unit explains how careful planning of water, soil and seed can raise yields while protecting the land for the next generation. Read each section slowly, look closely at the pictures, and talk about the ideas with your group before you move on to the lessons and activities that follow.</p>
    <div class="terrace-photo" role="img" aria-label="Photograph of misty rice terraces on a hillside"></div>
    <p class="body-text intro-column">Terraced fields hold water on steep hillsides and stop rich topsoil from washing away in heavy rain. Each step is levelled by hand and edged with a low wall of packed earth. Farmers open and close small gaps in these walls to move water from one terrace to the next. Good terraces also slow the flow of water, giving the roots of young plants more time to drink. When the terraces are well kept, the same land can feed a village for hundreds of years. In this unit you will learn how to plan, build and care for terraces, and how to choose crops that suit each level of the slope. Ask your teacher to show you examples from farms near your own home.</p>
    <svg class="footer-wave" viewBox="0 0 500 150" preserveAspectRatio="none" aria-hidden="true">
      <path d="M0 60 C180 10 360 40 500 90 L500 150 L0 150 Z" fill="var(--green-dark)"/>
      <path d="M0 72 C180 22 360 52 500 102 L500 150 L0 150 Z" fill="url(#wave-fill)"/>
    </svg>
    <div class="brand brand--light intro-left-brand">
      <span class="brand-dot"></span>
      <span class="brand-name">The Southern Meridian Collective<br>for Skills and Growth</span>
    </div>
  </article>

  <article class="page page--right intro-page">
    <h2 class="page-title">Introduction</h2>
    <div class="profile">
      <div class="portrait" role="img" aria-label="Portrait photograph of a construction expert"></div>
      <div class="profile-body">
        <p class="profile-name"><strong>Lina Santoso</strong> - Construction and Extraction</p>
        <p class="profile-text">Shares practical tips on building strong walls, drains and storage sheds that stand up to wet season storms and last for many years on the farm.</p>
      </div>
    </div>
    <div class="profile">
      <div class="portrait" role="img" aria-label="Portrait photograph of an engineering expert"></div>
      <div class="profile-body">
        <p class="profile-name"><strong>Arif Rahman</strong> - Engineering</p>
        <p class="profile-text">Explains how simple pumps, pipes and gates move water where it is needed and how to keep these tools working through every planting season.</p>
      </div>
    </div>
    <div class="profile">
      <div class="portrait" role="img" aria-label="Portrait photograph of an agriculture expert"></div>
      <div class="profile-body">
        <p class="profile-name"><strong>Tomas Reyes</strong> - Industrial Agriculture</p>
        <p class="profile-text">Guides you through soil testing, crop rotation and natural pest control so that your fields stay healthy and productive year after year.</p>
      </div>
    </div>
    <div class="body-text intro-closing">
      <p>Each expert has worked with farming communities for many years. Their advice appears in boxes like these throughout the unit, so look out for their names as you read the lessons and try the activities.</p>
      <p>Write down any questions you have and bring them to class. Sharing what you learn helps everyone on the farm grow stronger together.</p>
    </div>
    <svg class="footer-wave" viewBox="0 0 500 150" preserveAspectRatio="none" aria-hidden="true">
      <path d="M0 90 C150 40 330 20 500 60 L500 150 L0 150 Z" fill="var(--green-dark)"/>
      <path d="M0 102 C150 52 330 32 500 72 L500 150 L0 150 Z" fill="url(#wave-fill)"/>
    </svg>
    <div class="brand brand--light intro-right-brand">
      <span class="brand-dot"></span>
      <span class="brand-name">The Southern Meridian Collective<br>for Skills and Growth</span>
    </div>
  </article>
</section>

</body>
</html>
```